high performance web based fitness

High end online fitness portal. State of the art online fitness and high performance training. Also catering to all who are interested in a personally designed online training program by Olympic Gold Medalist "Dale Brennick" (dalebrennick.com)
Based in the Toronto area.
Online fitness consulting.
Including picture and video instruction of exercises. Downloadable fitness programs.
eCommerce ready.

(or just have skills to convert from site, i.e. wordpress, weebly)

Industry/Entity Type

Catering

```html
<!DOCTYPE html>
<html lang="en">
<head>
<meta charset="utf-8">
<title>VELOFIT – High Performance Online Fitness</title>
<link href="https://fonts.googleapis.com/css2?family=Source+Sans+3:wght@400;600;700&display=swap" rel="stylesheet">
<style>
  :root {
    --brand-blue: #1aaee6;
    --lime: #c3d21a;
    --olive: #a3ad12;
    --olive-dark: #8e9a0f;
    --cyan: #19d0f5;
    --cyan-deep: #12b8e0;
    --ink: #1b1b1b;
    --white: #ffffff;
    --footer: #e4e4e4;
    --green-btn: #5fae1e;
  }
  * { box-sizing: border-box; margin: 0; padding: 0; }
  html, body { width: 1152px; height: 1200px; overflow: hidden; background: var(--white); font-family: "Source Sans 3", Arial, sans-serif; color: var(--ink); }
  .page { position: relative; width: 1152px; height: 1200px; }

  .brand { position: absolute; left: 117px; top: 22px; font-size: 44px; font-weight: 700; color: var(--brand-blue); letter-spacing: 1px; }
  .search { position: absolute; left: 740px; top: 32px; width: 297px; height: 30px; border: 1px solid #d6d6d6; border-radius: 3px; display: flex; background: #fff; }
  .search span { flex: 1; padding: 5px 8px; font-size: 14px; color: #555; }
  .search b { width: 32px; background: var(--lime); border-radius: 0 3px 3px 0; display: flex; align-items: center; justify-content: center; }

  .nav { position: absolute; left: 0; top: 114px; width: 1152px; height: 48px; background: linear-gradient(#f1f1f1, #fff 40%); display: flex; align-items: center; padding-left: 115px; }
  .nav a { font-size: 13.5px; font-weight: 600; color: var(--ink); text-decoration: none; margin-right: 36px; }
  .nav a.active { background: var(--olive); color: #fff; height: 48px; line-height: 48px; padding: 0 12px; margin-right: 23px; }

  .hero { position: absolute; left: 0; top: 162px; width: 1152px; height: 462px; background: linear-gradient(180deg, #1d3d63 0%, #2f6fa3 35%, #1f3550 62%, #6b4a3e 80%, #8a5d4c 100%); }
  .hero h1 { position: absolute; left: 136px; top: 200px; font-size: 33px; font-weight: 700; color: var(--lime); letter-spacing: .5px; }
  .hero p { position: absolute; left: 136px; top: 275px; width: 380px; font-size: 16px; font-weight: 600; color: #fff; line-height: 21px; }
  .dots { position: absolute; left: 125px; top: 425px; display: flex; gap: 6px; }
  .dots i { width: 14px; height: 14px; border-radius: 50%; background: #1b2d4a; }
  .dots i:first-child { background: #e6e6e6; }

  .panel { position: absolute; top: 643px; width: 288px; height: 374px; background: var(--cyan); }
  .panel h2 { font-size: 23px; font-weight: 700; color: #fff; padding: 9px 9px 0; height: 49px; border-bottom: 1px dashed #0c9fc4; text-shadow: 0 1px 1px rgba(0,0,0,.2); }
  .welcome p { font-family: Arial, sans-serif; font-size: 11.3px; line-height: 15.4px; text-align: justify; padding: 0 13px; margin-top: 15px; }
  .panel .rule { position: absolute; left: 0; top: 320px; width: 100%; border-top: 1px dashed #0c9fc4; }
  .more { position: absolute; left: 0; top: 331px; height: 35px; width: 105px; background: var(--lime); clip-path: polygon(0 0, 85% 0, 100% 50%, 85% 100%, 0 100%); font-size: 13px; font-weight: 700; line-height: 35px; padding-left: 13px; color: #222; }

  .video { position: absolute; left: 9px; top: 65px; width: 270px; height: 208px; background: linear-gradient(135deg, #2a2a2a, #5a4a40 55%, #1a1a1a); }
  .controls { position: absolute; left: 9px; top: 273px; width: 270px; height: 20px; background: #eee; display: flex; align-items: center; padding: 0 7px; gap: 8px; font-size: 6px; color: #555; }
  .controls .bar { flex: 1; height: 5px; border-radius: 3px; background: #ccc; }

  .thumb { position: absolute; width: 124px; height: 113px; background: #fff; padding: 9px; }
  .thumb div { width: 100%; height: 100%; }

  .download { position: absolute; left: 115px; top: 1037px; width: 922px; height: 86px; background: var(--olive); display: flex; align-items: center; }
  .download h3 { font-size: 28px; font-weight: 700; color: #fff; margin-left: 26px; letter-spacing: .3px; }
  .btn { position: absolute; left: 626px; top: 18px; width: 276px; height: 52px; border-radius: 6px; border: 2px solid #3f7d10; background: linear-gradient(#8fd13a, var(--green-btn) 55%, #3d8d12); display: flex; align-items: center; padding-left: 12px; gap: 18px; font-size: 31px; font-weight: 700; color: #fff; }

  .footer { position: absolute; left: 0; top: 1135px; width: 1152px; height: 65px; background: var(--footer); }
  .footer small { position: absolute; left: 117px; top: 23px; font-size: 11px; font-weight: 700; }
  .social { position: absolute; left: 847px; top: 13px; display: flex; gap: 12px; }
  .social i { width: 36px; height: 36px; border-radius: 50%; border: 3px solid #fff; box-shadow: 0 1px 3px rgba(0,0,0,.3); }
</style>
</head>
<body>
<div class="page">
  <div class="brand">VELOFIT</div>
  <div class="search"><span>Search</span><b><svg width="14" height="14" viewBox="0 0 14 14"><circle cx="5" cy="5" r="3.6" fill="none" stroke="#fff" stroke-width="2"/><path d="M8 8l5 5" stroke="#fff" stroke-width="2.4"/></svg></b></div>

  <nav class="nav">
    <a class="active">HOME</a><a>ABOUT US</a><a>SERVICES</a><a>TESTIMONIALS</a><a>BOOK AN APPOINTMENT</a><a>PHOTO ALBUM</a><a>FAQ</a><a>BLOG</a><a>CONTACT US</a>
  </nav>

  <section class="hero" role="img" aria-label="Sprinter in starting blocks on a stadium track under floodlights at dusk">
    <h1>CONSULTING</h1>
    <p>PERSONALIZE YOUR FITNESS EXPERIENCE...<br>ONE-ON-ONE CONSULTING TO OPTIMIZE YOUR PROGRAM...</p>
    <div class="dots"><i></i><i></i><i></i></div>
  </section>

  <section class="panel welcome" style="left:115px">
    <h2>WELCOME</h2>
    <p>ciatis unde omnis iste natus error sit voluptatem accusantium doloremque laudantium, totam rem aperiam,</p>
    <p>eaque ipsa quae ab illo inventore veritatis et quasi architecto beatae vitae dicta sunt explicabo. Nemo enim ipsam voluptatem quia voluptas sit aspernatur aut odit aut fugit, sed quia consequuntur magni dolores eos qui ratione voluptatem sequi nesciunt. Neque porro quisquam est, qui dolorem ipsum quia dolor sit amet, consectetur, adipisci velit, sed quia non numquam eius modi tempora incidunt ut labore et dolore magnam aliquam quaerat voluptatem. Ut enim ad minima veniam, quis nostrum exercitationem ullam corporis suscipit laboriosam, nisi ut aliquid ex ea commodi consequatur? Quis autem vel</p>
    <div class="rule"></div>
    <div class="more">VIEW MORE</div>
  </section>

  <section class="panel" style="left:432px">
    <h2>WATCH OUR VIDEO</h2>
    <div class="video" role="img" aria-label="Video still of a coach speaking and pointing at a podium">
      <svg style="position:absolute;left:107px;top:84px" width="54" height="54" viewBox="0 0 54 54"><circle cx="27" cy="27" r="25" fill="#1a4f8a" stroke="#0d2440" stroke-width="3"/><circle cx="27" cy="27" r="17" fill="#3a8fd8"/><path d="M22 18l13 9-13 9z" fill="#fff"/></svg>
    </div>
    <div class="controls"><svg width="8" height="9"><path d="M0 0l8 4.5L0 9z" fill="#333"/></svg><div class="bar"></div><span>0:20/2:00</span></div>
    <div class="rule"></div>
    <div class="more">VIEW MORE</div>
  </section>

  <section class="panel" style="left:749px">
    <h2>PHOTO GALLERY</h2>
    <div class="thumb" style="left:16px;top:63px"><div role="img" aria-label="Two athletes posing together" style="background:linear-gradient(135deg,#3a3a3a,#8a7a6a)"></div></div>
    <div class="thumb" style="left:152px;top:63px"><div role="img" aria-label="Sprinter running on a track" style="background:linear-gradient(135deg,#cfcfcf,#777)"></div></div>
    <div class="thumb" style="left:16px;top:190px"><div role="img" aria-label="Athlete portrait in team jacket" style="background:linear-gradient(135deg,#8a5a40,#e8e8e8 60%,#17324a)"></div></div>
    <div class="thumb" style="left:152px;top:190px"><div role="img" aria-label="Event poster of hurdlers in a race" style="background:linear-gradient(135deg,#2c6aa3,#b57a4a 60%,#8fb4d0)"></div></div>
    <div class="rule"></div>
    <div class="more">VIEW MORE</div>
  </section>

  <section class="download">
    <svg style="margin-left:22px" width="66" height="68" viewBox="0 0 66 68"><path d="M12 2h30l14 14v48H12z" fill="#f3f3f3" stroke="#ccc"/><path d="M42 2v14h14" fill="#ddd"/><rect x="2" y="28" width="62" height="22" rx="3" fill="#c0201e"/><text x="33" y="45" font-family="Source Sans 3, Arial, sans-serif" font-weight="700" font-size="18" fill="#fff" text-anchor="middle">PDF</text></svg>
    <h3>DOWNLOAD OUR FITNESS PROGRAM</h3>
    <div class="btn"><svg width="38" height="38" viewBox="0 0 38 38"><circle cx="19" cy="19" r="18" fill="#2e3a1e"/><circle cx="19" cy="19" r="14" fill="#8a3ad8"/><path d="M12 16l7 7 7-7" fill="none" stroke="#1d0a33" stroke-width="3.5"/></svg>DOWNLOAD</div>
  </section>

  <footer class="footer">
    <small>© 2013 VELOFIT. ALL RIGHTS RESERVED.</small>
    <div class="social">
      <i style="background:#3b5b9a"></i><i style="background:#27a3df"></i><i style="background:#d8382c"></i><i style="background:#c7201a"></i>
    </div>
  </footer>
</div>
</body>
</html>
```